Laser Tattoo Removal Business Cards

We are looking for a professional business card design for a laser tattoo removal business. Ideally looking for a black business card design. The name of the business is Lumen Ink Clearing. We place our cards at local tattoo shops so we ideally are looking for something trendy/edgy to draw both male and female clientele in.

Target Market(s)

Male/Female ages 18-60

Contact Information for Business Card

black background ideally.. hoping to stay within greys, whites and black

Font styles to use
Serif
Sans Serif

Colors
121212
a9a9a9
5c5c5c
f5f5f5
ffffff
7f7f7f
606060
848484
9d9d9d

Requirements
Must have
• Employee Info:
• Marisol Dunmore
• Chief Executive Offer
• m: 919.555.0143
• w: 919.555.0178
• f: 919.555.0192
• mdunmore@lumeninkclearing.com
• Address:
• 4185 Fenwick Pkwy, Suite 210
• Marlow Heights, NC 27890
• Website:
• www.lumeninkclearing.com
Nice to have
• Myabe business name on back or logo on back and employee info on the front

```html
<!DOCTYPE html>
<html lang="en">
<head>
<meta charset="utf-8">
<title>Lumen Ink Clearing — Business Cards</title>
<link rel="stylesheet" href="https://fonts.googleapis.com/css2?family=Josefin+Sans:wght@400&family=Lato:wght@400;700&display=swap">
<style>
  :root {
    --ink: #121212;
    --paper: #ffffff;
    --paper-soft: #f5f5f5;
    --grey-light: #a9a9a9;
    --grey-mid: #7f7f7f;
    --grey-dark: #5c5c5c;
    --backdrop: #2a2a2a;
  }
  * { box-sizing: border-box; margin: 0; padding: 0; }
  html, body { width: 1200px; height: 900px; overflow: hidden; }
  body {
    background: var(--backdrop);
    font-family: "Lato", sans-serif;
    position: relative;
  }
  .card {
    position: absolute;
    left: 320px;
    width: 560px;
    height: 320px;
    border-radius: 14px;
    overflow: hidden;
  }
  .card--front { top: 90px; background: var(--ink); }
  .card--back { top: 470px; background: var(--ink); display: flex; }

  .brand {
    display: flex;
    align-items: center;
    justify-content: center;
    gap: 14px;
  }
  .brand__mark { width: 14px; height: 14px; flex: none; }
  .brand__name {
    font-family: "Josefin Sans", sans-serif;
    font-weight: 400;
    text-transform: uppercase;
    letter-spacing: 0.12em;
    line-height: 1;
    white-space: nowrap;
  }

  .card--front .brand { position: absolute; left: 40px; right: 40px; top: 116px; }
  .card--front .brand__name { color: var(--paper); font-size: 30px; }
  .card--front .brand__mark { background: var(--paper); }

  .web-band {
    position: absolute;
    left: 0; right: 0; bottom: 0;
    height: 64px;
    background: var(--paper);
    display: flex;
    align-items: center;
    justify-content: center;
  }
  .web-band__url {
    color: var(--ink);
    font-weight: 700;
    font-size: 15px;
    letter-spacing: 0.2em;
  }

  .back__logo-panel {
    width: 250px;
    height: 100%;
    background: var(--paper-soft);
    display: flex;
    align-items: center;
    justify-content: center;
  }
  .back__logo-panel .brand { flex-direction: column; gap: 10px; }
  .back__logo-panel .brand__name { color: var(--ink); font-size: 24px; text-align: center; line-height: 1.25; }
  .back__logo-panel .brand__mark { background: var(--ink); }

  .divider {
    width: 30px;
    height: 100%;
    background: var(--paper);
    display: flex;
    gap: 6px;
    padding-left: 4px;
  }
  .divider__rule { width: 5px; height: 100%; background: var(--ink); }

  .contact {
    flex: 1;
    padding: 34px 24px 0 34px;
    color: var(--paper);
  }
  .contact__name { font-size: 20px; font-weight: 400; }
  .contact__name b { font-weight: 700; }
  .contact__title { font-size: 12px; color: var(--paper-soft); margin-top: 3px; }
  .contact__address { margin-top: 52px; font-size: 13px; font-weight: 700; line-height: 1.45; }
  .contact__list { list-style: none; margin-top: 8px; font-size: 13px; }
  .contact__list li { display: flex; align-items: center; gap: 12px; height: 22px; white-space: nowrap; }
  .contact__icon { width: 14px; height: 14px; fill: var(--paper); flex: none; }
</style>
</head>
<body>

  <section class="card card--front" aria-label="Card front">
    <div class="brand">
      <span class="brand__mark"></span>
      <span class="brand__name">Lumen Ink Clearing</span>
    </div>
    <div class="web-band">
      <span class="web-band__url">www.lumeninkclearing.com</span>
    </div>
  </section>

  <section class="card card--back" aria-label="Card back">
    <div class="back__logo-panel">
      <div class="brand">
        <span class="brand__name">Lumen Ink<br>Clearing</span>
        <span class="brand__mark"></span>
      </div>
    </div>
    <div class="divider">
      <span class="divider__rule"></span>
      <span class="divider__rule"></span>
    </div>
    <div class="contact">
      <h1 class="contact__name">Marisol <b>Dunmore</b></h1>
      <p class="contact__title">Chief Executive Offer</p>
      <p class="contact__address">4185 Fenwick Pkwy, Suite 210<br>Marlow Heights, NC 27890</p>
      <ul class="contact__list">
        <li>
          <svg class="contact__icon" viewBox="0 0 16 16" aria-hidden="true"><path d="M1 5c0-2 3-3 7-3s7 1 7 3v1.5h-3.5V5h-7v1.5H1zM4 8l1.5-2h5L12 8v5H4zm4 1a1.5 1.5 0 1 0 0 3 1.5 1.5 0 0 0 0-3z"/></svg>
          <span>919.555.0143</span>
        </li>
        <li>
          <svg class="contact__icon" viewBox="0 0 16 16" aria-hidden="true"><path d="M4 1h8v4H4zM1 6h14v6h-3v3H4v-3H1zm4 4v4h6v-4z"/></svg>
          <span>919.555.0192</span>
        </li>
        <li>
          <svg class="contact__icon" viewBox="0 0 16 16" aria-hidden="true"><path d="M1 3h14v10H1zm1.5 1.2L8 8.5l5.5-4.3z"/></svg>
          <span>mdunmore@lumeninkclearing.com</span>
        </li>
      </ul>
    </div>
  </section>

</body>
</html>
```